FINANCIAL ADVISOR WORDPRESS WEBSITE

Hello, Here% 26 # 39; s the project. I just want a copy of this website .. I https://www.cabinet-velorane.fr/lp/velorane/conseil-epargne-horizon.php?wh=campagne%26amp;ref=Xk7TbQwRmZ3LpVaYcN2sHdF-_J_Q8eW4uGzKoTnB61Mv_ExyRrLsPiUq_58w-4jDhOa_Z93V_K2aBtDfGh7-QLmn_xyZ just want you to make it work under wordpress as i can update easily. Please find the logo attached. If you can install it in my web host it would be great. Thanks Armand.

Number of Pages Required

3 page

Font styles to use
Serif

Colors
1f66ae

Requirements
Must have
• WORDPRESS ONLY

```html
<!DOCTYPE html>
<html lang="en">
<head>
<meta charset="utf-8">
<title>Velorane Conseil – Wealth management</title>
<link href="https://fonts.googleapis.com/css2?family=Montserrat:wght@400;500;600&display=swap" rel="stylesheet">
<style>
  :root{
    --bg-top:#8aa3d3;
    --bg-bottom:#6b8dc6;
    --header:rgba(82,104,152,.72);
    --white:#ffffff;
    --field-text:#5d6270;
    --btn-start:#ff8a4c;
    --btn-end:#ffd35e;
    --tick:#2a3fe0;
    --brand:#1f2433;
  }
  *{box-sizing:border-box;margin:0;padding:0}
  html,body{width:1200px;height:695px;overflow:hidden}
  body{font-family:'Montserrat',sans-serif;color:var(--white);
    background:linear-gradient(100deg,var(--bg-top) 0%,#7f9bcf 45%,var(--bg-bottom) 100%);position:relative}
  .scene{position:absolute;left:0;top:80px;width:1200px;height:615px}
  .site-header{position:absolute;left:0;top:0;width:1200px;height:80px;background:var(--header)}
  .brand{position:absolute;left:113px;top:30px;color:var(--brand);font-size:18px;font-weight:600;line-height:22px}
  .nav{position:absolute;left:499px;top:31px;display:flex;gap:22px;font-size:12px;font-weight:600;list-style:none}
  .hero-left{position:absolute;left:111px;top:158px;width:390px}
  .hero-title{font-size:24px;font-weight:500;line-height:26.5px;text-transform:uppercase}
  .hero-sub{font-size:12px;font-weight:600;line-height:18px;margin-top:13px}
  .form{position:absolute;left:113px;top:308px;width:384px}
  .field{position:absolute;height:33px;background:var(--white);border:1px solid #dfe3ea;
    color:var(--field-text);font-size:12px;font-weight:500;line-height:31px;padding-left:9px}
  .field.select{color:#2b2f38;padding-left:12px}
  .field.select::after{content:"▾";position:absolute;right:6px;top:0;font-size:9px;color:#222}
  .btn{position:absolute;left:111px;top:547px;width:388px;height:37px;border-radius:2px;
    background:linear-gradient(90deg,var(--btn-start),var(--btn-end));
    font-size:12px;font-weight:600;text-align:center;line-height:37px}
  .reassure{position:absolute;left:111px;top:615px;width:388px;text-align:center;font-size:12px;font-weight:500}
  .hero-right{position:absolute;left:534px;top:239px;width:440px;text-align:center}
  .award{font-size:15.5px;line-height:20.5px;text-transform:uppercase;font-weight:500}
  .support{font-size:15.5px;line-height:20.5px;font-weight:600;margin-top:14px}
  .facts{position:absolute;left:626px;top:406px;width:336px;list-style:none;font-size:14px;line-height:22.5px;font-weight:500}
  .facts li{margin-bottom:4px}
  .facts svg{vertical-align:middle;margin-right:4px}
</style>
</head>
<body>
  <svg class="scene" viewBox="0 0 1200 615" role="img" aria-label="Illustration: a businessman standing in a blue room casting a large caped shadow on the wall">
    <defs>
      <linearGradient id="sceneShade" x1="0" y1="0" x2="1" y2="0">
        <stop offset="0" stop-color="#6f8ec6" stop-opacity="0"/>
        <stop offset="1" stop-color="#5473ad" stop-opacity=".5"/>
      </linearGradient>
    </defs>
    <rect x="760" y="0" width="440" height="615" fill="url(#sceneShade)"/>
    <polygon points="0,615 0,560 760,420 1200,380 1200,615" fill="#a4b6e0" opacity=".35"/>
  </svg>

  <header class="site-header">
    <div class="brand">Velorane Conseil</div>
    <ul class="nav">
      <li>Tax exemption</li><li>Pinel Law</li><li>Testimonials</li><li>Key figures</li><li>Our values</li>
    </ul>
  </header>

  <section class="hero-left">
    <h1 class="hero-title">For the management of your wealth, trust a champion!</h1>
    <p class="hero-sub">Benefit from a free and non-binding balance sheet, to find out what tax reduction you are entitled to</p>
  </section>

  <form class="form">
    <div class="field select" style="left:0;top:0;width:179px">Tax bracket</div>
    <div class="field select" style="left:204px;top:0;width:180px">year of birth</div>
    <div class="field" style="left:0;top:48px;width:384px">Adresse email</div>
    <div class="field" style="left:0;top:97px;width:384px">Téléphone</div>
    <div class="field" style="left:0;top:145px;width:384px">Code postal</div>
    <div class="field" style="left:0;top:193px;width:179px">Nom</div>
    <div class="field" style="left:204px;top:193px;width:180px">Prénom</div>
  </form>
  <div class="btn">Personalized Free Assessment</div>
  <p class="reassure">100% Free - Confidential - No Commitment</p>

  <section class="hero-right">
    <p class="award">The Velorane group was elected growth champion by Le Journal Éco in 2017 and 2018, thanks to its quality of monitoring and its solutions geared to your performance.</p>
    <p class="support">Our team supports you to:<br>Tax exemption - Build real estate assets - Ensure your retirement - Optimize your investments</p>
  </section>

  <ul class="facts">
    <li><svg width="10" height="8" viewBox="0 0 10 8"><path d="M1 4l3 3 5-6" fill="none" stroke="var(--tick)" stroke-width="1.6"/></svg>250 advisers throughout France, including one dedicated to your geographic area.</li>
    <li><svg width="10" height="8" viewBox="0 0 10 8"><path d="M1 4l3 3 5-6" fill="none" stroke="var(--tick)" stroke-width="1.6"/></svg>35,000 asset assessments carried out in 2017</li>
    <li><svg width="10" height="8" viewBox="0 0 10 8"><path d="M1 4l3 3 5-6" fill="none" stroke="var(--tick)" stroke-width="1.6"/></svg> 50 million euros in taxes saved by our customers</li>
  </ul>
</body>
</html>
```